Site for entrepreneurs/small businesses needs Logo, Homepage

Looking for a logo, either an icon, or stylized text, or a combination of both, and a home page design which fits with it. The logo will be for use on the public website as well as for printed collateral (business cards, post cards, brochures and various other marketing materials).

The site is called MiraPlume (MiraPlume.com). This is to be a national, and eventually an international brand. The new service will provide an easy-to-use platform for entrepreneurs to build their business and web presence together in an integrated way which allows them to focus on their core competency.

The site/service will be dead-simple to use, A/B/C, 1/2/3. We will want some sort of "Get started for FREE" promotional space to collect the person's email address with multiple points of interest which guide the user back to this one call to action: sign up for free. We will feature editorial/blog stories, customer testimonials, and present several key features the the reader just can't live without if they are starting a new business.

Criteria:
* Refer to our comparable sites/logos in the design document attached
* Incorporate our color scheme (but complementary colors welcome)
* No Serif fonts!
* No photo-realistic elements for logo
* Logo must present well in gray scale and/or black/white (for printed materials)
* Strokes/borders that are wider to promote simplicity (vs. thin/precise lines which promote technical complexity)

Inspirations:
* Creative/Custom (but legible) fonts
* Excitement, energetic, jumping for joy
* Karate / Ninja / Power / Precision
* Dance Moves
* Regional influences: California, Silicon Valley, West Coast, Surf City, Beaches, Sunset
* Simple/easy, no-brainer solutions

Target Market(s)

Small Businesses / Entrepreneurs

Logo Text

MiraPlume or MiraPlume.com

Number of Pages Required

1 page

Font styles to use
Sans Serif
Decorative

Requirements
Must have
• See the attached style guide (PDF)

```html
<!DOCTYPE html>
<html lang="en">
<head>
<meta charset="utf-8">
<title>MiraPlume – Build your business</title>
<link rel="stylesheet" href="https://fonts.googleapis.com/css2?family=Josefin+Sans:wght@400;600;700&family=Open+Sans:wght@400;600;700&display=swap">
<style>
  :root{
    --navy:#14295c;
    --navy-deep:#0f1f4a;
    --violet:#a98bf0;
    --blue:#7f95ea;
    --lilac:#e6dcfb;
    --lilac-soft:#f1ecfd;
    --pink:#c78bf0;
    --text:#1d2a55;
    --muted:#7a80a0;
    --white:#ffffff;
    --gold:#f2b64a;
  }
  *{box-sizing:border-box;margin:0;padding:0}
  html,body{width:1200px;height:3004px;overflow:hidden}
  body{position:relative;background:var(--white);font-family:"Open Sans",sans-serif;color:var(--text)}
  .backdrop{position:absolute;left:0;top:0;width:1200px;height:3004px}
  .abs{position:absolute;z-index:2}
  .heading{font-family:"Josefin Sans",sans-serif;font-weight:600;color:var(--navy);line-height:1.15}
  .pill{display:flex;align-items:center;justify-content:center;border-radius:20px;font-size:13px;font-weight:600;text-decoration:none}
  .pill-dark{background:var(--navy);color:var(--white)}
  .pill-light{background:var(--white);color:var(--navy)}
  .pill-violet{background:linear-gradient(90deg,var(--violet),var(--pink));color:var(--white)}
  .abs.art{border-radius:24px;z-index:1}

  /* header */
  .menu-icon{left:140px;top:64px;width:26px;height:18px}
  .brand{left:186px;top:60px;display:flex;align-items:center;gap:10px;font-family:"Josefin Sans",sans-serif;font-weight:700;font-size:24px;color:var(--white)}
  .brand-mark{width:14px;height:14px;border-radius:50%;background:var(--white)}
  .nav-try{left:788px;top:56px;width:132px;height:40px}
  .nav-contact{left:944px;top:56px;width:136px;height:40px}

  /* hero */
  .hero-title{left:144px;top:244px;width:440px;font-size:44px;color:var(--white)}
  .hero-sub{left:144px;top:352px;width:340px;font-size:13px;color:var(--white);opacity:.9;line-height:1.5}
  .hero-input{left:144px;top:404px;width:300px;height:30px;border-bottom:1.5px solid rgba(255,255,255,.7);font-size:13px;color:rgba(255,255,255,.75);padding-top:4px}
  .hero-cta{left:144px;top:464px;width:176px;height:40px}
  .hero-art{left:610px;top:120px;width:560px;height:610px;background:linear-gradient(150deg,#3a4f9a 0%,#5c74d6 45%,#26386f 100%);opacity:.9}
  .calc-art{left:320px;top:870px;width:290px;height:250px;background:linear-gradient(160deg,#4a63c8,#1f3475)}

  /* calculate */
  .calc-title{right:120px;top:816px;width:320px;text-align:right;font-size:38px}
  .calc-sub{right:120px;top:960px;width:300px;text-align:right;font-size:12px;color:var(--muted)}
  .calc-cta{left:880px;top:992px;width:180px;height:34px}

  /* features */
  .feat-title{left:144px;top:1266px;font-size:36px}
  .feature{left:168px;width:330px;display:flex;gap:22px}
  .feature svg{flex:none;width:26px;height:26px;margin-top:4px}
  .feature h3{font-size:13px;font-weight:700;color:var(--navy);margin-bottom:4px}
  .feature p{font-size:11px;line-height:1.5;color:var(--muted)}
  .feat-cta{left:144px;top:1684px;width:164px;height:38px}
  .feat-art{left:560px;top:1140px;width:540px;height:550px;background:linear-gradient(160deg,#e9e6f8,#b9c6f3 55%,#3a4f9a)}

  /* testimonial */
  .quote-title{left:0;top:1828px;width:1200px;text-align:center;font-size:36px}
  .avatar{left:560px;top:1938px;width:80px;height:80px;border-radius:50%;background:linear-gradient(160deg,#f3d3b8,#d79a7c);border:4px solid var(--white)}
  .quote-name{left:0;top:2026px;width:1200px;text-align:center;font-size:13px;font-weight:700;color:var(--navy)}
  .quote-text{left:330px;top:2052px;width:540px;text-align:center;font-size:12px;line-height:1.55;color:var(--muted)}
  .dots{left:580px;top:2104px;width:40px;display:flex;justify-content:center;gap:10px}
  .dots span{width:8px;height:8px;border-radius:50%;background:#c7c9d8}
  .dots span.on{background:var(--navy)}

  /* help */
  .video-art{left:120px;top:2216px;width:690px;height:510px;background:linear-gradient(160deg,#dfe6fb,#8ea2e6 60%,#2a3e82)}
  .help-card{left:660px;top:2356px;width:414px;height:204px;background:var(--white);border-radius:4px;box-shadow:0 10px 30px rgba(40,40,100,.08)}
  .help-title{left:688px;top:2388px;font-size:38px}
  .help-sub{left:688px;top:2438px;font-size:12px;color:var(--muted)}

  /* footer */
  .footer-nav{left:316px;top:2832px;width:576px;display:flex;justify-content:space-between;font-size:12px;font-weight:700;color:var(--navy);letter-spacing:.5px}
  .socials{left:516px;top:2908px;display:flex;gap:24px}
  .socials span{width:14px;height:14px;border-radius:50%;background:var(--gold)}
</style>
</head>
<body>

<svg class="backdrop" viewBox="0 0 1200 3004" aria-hidden="true">
  <defs>
    <linearGradient id="heroGrad" x1="0" y1="0" x2="1" y2="1">
      <stop offset="0" stop-color="#a68cf0"/>
      <stop offset=".55" stop-color="#8a98ec"/>
      <stop offset="1" stop-color="#c7b4f6"/>
    </linearGradient>
    <linearGradient id="softGrad" x1="0" y1="0" x2="1" y2="0">
      <stop offset="0" stop-color="#f1ecfd"/>
      <stop offset="1" stop-color="#d9cbfa"/>
    </linearGradient>
    <linearGradient id="footGrad" x1="0" y1="0" x2="0" y2="1">
      <stop offset="0" stop-color="#ffffff"/>
      <stop offset="1" stop-color="#eef0fc"/>
    </linearGradient>
  </defs>
  <path d="M0 0H1200V560C1130 600 1050 520 960 560C880 600 840 700 740 720C620 740 560 640 450 650C300 665 260 780 0 800Z" fill="url(#heroGrad)"/>
  <circle cx="240" cy="800" r="230" fill="var(--navy-deep)"/>
  <circle cx="1120" cy="1410" r="210" fill="var(--navy)"/>
  <path d="M640 1800C760 1730 980 1740 1090 1820C1200 1900 1160 2030 1060 2080C980 2120 900 2110 860 2160H340C260 2120 300 2010 380 1960C450 1915 540 1860 640 1800Z" fill="url(#softGrad)" opacity=".7"/>
  <path d="M1200 2200C1080 2220 960 2290 920 2380C880 2470 960 2560 1080 2580C1150 2590 1200 2560 1200 2560Z" fill="#c9b6f7" opacity=".8"/>
  <circle cx="1160" cy="2650" r="130" fill="var(--navy)"/>
  <rect x="0" y="2740" width="1200" height="264" fill="url(#footGrad)"/>
</svg>

<!-- header -->
<svg class="abs menu-icon" viewBox="0 0 26 18" aria-label="Menu"><rect width="26" height="3" rx="1.5" fill="#fff"/><rect y="7.5" width="26" height="3" rx="1.5" fill="#fff"/><rect y="15" width="26" height="3" rx="1.5" fill="#fff"/></svg>
<div class="abs brand"><span class="brand-mark"></span>MiraPlume</div>
<a class="abs pill pill-light nav-try" href="#">Try it Free</a>
<a class="abs pill pill-dark nav-contact" href="#">Contact Us</a>

<!-- hero -->
<div class="abs art hero-art" role="img" aria-label="Isometric illustration of a desktop computer with keyboard, mouse, gears and clouds"></div>
<h1 class="abs heading hero-title">For entrepreneurs to build their business</h1>
<p class="abs hero-sub">Build a site, a brand and a plan in one simple place.</p>
<div class="abs hero-input">Your email address</div>
<a class="abs pill pill-dark hero-cta" href="#">Get started for free</a>
<div class="abs art calc-art" role="img" aria-label="Isometric illustration of a large calculator with a small figure standing on it"></div>

<!-- calculate -->
<h2 class="abs heading calc-title">Calculate the Cost to kickstart your idea</h2>
<p class="abs calc-sub">Estimate your launch budget in three quick steps.</p>
<a class="abs pill pill-violet calc-cta" href="#">Get a Free Quote</a>

<!-- features -->
<div class="abs art feat-art" role="img" aria-label="Isometric illustration of a team working around a laptop, charts and books"></div>
<h2 class="abs heading feat-title">MiraPlume<br>Key features</h2>
<div class="abs feature" style="top:1386px">
  <svg viewBox="0 0 24 24"><path d="M3 11L21 3L14 21L11 13Z" fill="none" stroke="var(--navy)" stroke-width="2" stroke-linejoin="round"/></svg>
  <div><h3>Easy Setup</h3><p>Pick a template, add your details and go live in minutes without any code.</p></div>
</div>
<div class="abs feature" style="top:1476px">
  <svg viewBox="0 0 24 24"><path d="M3 10H7V21H3Z M7 11L11 3C13 3 14 4 13.5 7L13 9H19C20.5 9 21.5 10.5 21 12L19 19C18.7 20.2 17.8 21 16.5 21H7" fill="none" stroke="var(--navy)" stroke-width="2" stroke-linejoin="round"/></svg>
  <div><h3>Grow Faster</h3><p>Marketing tools that help new customers find you and keep coming back for more.</p></div>
</div>
<div class="abs feature" style="top:1568px">
  <svg viewBox="0 0 24 24"><circle cx="12" cy="8" r="4.5" fill="none" stroke="var(--navy)" stroke-width="2"/><path d="M4 21C4 16 8 14 12 14C16 14 20 16 20 21Z" fill="none" stroke="var(--navy)" stroke-width="2" stroke-linejoin="round"/></svg>
  <div><h3>Own Your Brand</h3><p>Your logo, your domain and your store, all managed from one calm dashboard.</p></div>
</div>
<a class="abs pill pill-violet feat-cta" href="#">Learn More</a>

<!-- testimonial -->
<h2 class="abs heading quote-title">What do<br>they say about us?</h2>
<div class="abs avatar" role="img" aria-label="Customer portrait"></div>
<p class="abs quote-name">Nora, CEO</p>
<p class="abs quote-text">MiraPlume gave us a website, invoices and email in one afternoon. We finally spend our time on the work we love.</p>
<div class="abs dots"><span class="on"></span><span></span></div>

<!-- help -->
<div class="abs art video-art" role="img" aria-label="Illustration of a laptop playing a video with small figures standing beside it"></div>
<div class="abs help-card"></div>
<h2 class="abs heading help-title">Still Confused?</h2>
<p class="abs help-sub">Talk to our friendly team today.</p>

<!-- footer -->
<nav class="abs footer-nav">
  <span>GET STARTED</span><span>TEAM</span><span>CAREERS</span><span>PRICE</span><span>PARTNERS</span><span>CONTACT US</span>
</nav>
<div class="abs socials" aria-label="Social links"><span></span><span></span><span></span><span></span><span></span></div>

</body>
</html>
```